Pale Ridge Software

We are a software company selling endpoint visibility, access and security technology to enterprise-level IT departments.

Our technology helps organizations gain comprehensive visibility into and control over devices accessing their corporate network so they can quickly identify and address suspicious activity on the network that could lead to potential threats like data breaches.

This technology can cost organizations upwards of $1M - depending on the size of the organization. Our primary clients are Summit 3,000 companies.

We want a professional, polished business card to represent our new brand.

Info fields to include on the card:
Name
Job Title
Office Phone #
Cell Phone #
Email address
Address: 4172 Wexmoor Pond Ave., Ste. 2600, Bloomington, MN 55819
Website address: www.paleridgesoftware.example
Tagline: Discover the edge. Optimize the whole.

Logo files and color specs document are attached. Would like color scheme to coordinate with the logo.

Also looking at stationary/envelope designs in conjunction with the business card designs. Received very few designs that included the stationary.

```html
<!DOCTYPE html>
<html lang="en">
<head>
<meta charset="utf-8">
<title>Pale Ridge Software – Business Card</title>
<link rel="stylesheet" href="https://fonts.googleapis.com/css2?family=Ubuntu:ital,wght@0,400;0,500;1,400&display=swap">
<style>
  :root {
    --backdrop: #d6d4d3;
    --brand-red: #8c2024;
    --card-grey: #8a8a8c;
    --tab-white: #f4f4f4;
    --text-white: #ffffff;
    --label-red: #a5262b;
  }
  * { margin: 0; padding: 0; box-sizing: border-box; }
  html, body {
    width: 1200px; height: 1000px; overflow: hidden;
    background: var(--backdrop);
    font-family: "Ubuntu", "Helvetica Neue", Arial, sans-serif;
  }
  .stage {
    position: relative; width: 1200px; height: 1000px;
  }
  .card {
    position: absolute; top: 325px;
    width: 540px; height: 350px;
    overflow: hidden;
  }
  .card--front { left: 40px; background: var(--brand-red); }
  .card--back { left: 620px; background: var(--card-grey); }

  .brand {
    display: flex; align-items: center; gap: 14px;
    font-weight: 500; text-transform: uppercase; letter-spacing: 0.12em;
  }
  .brand__mark { width: 16px; height: 16px; }
  .card--front .brand {
    position: absolute; left: 50%; top: 50%;
    transform: translate(-50%, -50%);
    color: var(--text-white); font-size: 24px; white-space: nowrap;
  }
  .card--front .brand__mark { background: var(--text-white); }

  .back-texture {
    position: absolute; left: 0; top: 30px; width: 190px; height: 290px;
    background: radial-gradient(ellipse at 35% 50%, rgba(255,255,255,0.16), rgba(255,255,255,0) 70%);
  }

  .holder {
    position: absolute; left: 42px; top: 58px; color: var(--text-white);
  }
  .holder__name { font-size: 26px; font-weight: 400; line-height: 1.1; }
  .holder__title {
    font-size: 16px; font-style: italic; color: var(--label-red); margin-top: 3px;
  }

  .brand-tab { position: absolute; left: 208px; top: 60px; width: 332px; height: 58px; }
  .brand-tab svg { position: absolute; inset: 0; }
  .card--back .brand {
    position: absolute; left: 100px; top: 50%; transform: translateY(-50%);
    color: var(--brand-red); font-size: 15px; white-space: nowrap;
  }
  .card--back .brand__mark { width: 12px; height: 12px; background: var(--brand-red); }

  .contact {
    position: absolute; right: 37px; top: 208px;
    text-align: right; font-size: 13.5px; line-height: 18px;
    color: var(--text-white); list-style: none;
  }
  .contact__label { color: var(--label-red); }
</style>
</head>
<body>
<main class="stage">
  <section class="card card--front" aria-label="Card front">
    <div class="brand">
      <span class="brand__mark"></span>
      <span class="brand__name">Pale Ridge Software</span>
    </div>
  </section>

  <section class="card card--back" aria-label="Card back">
    <div class="back-texture" role="img" aria-label="Soft dotted brand texture area"></div>

    <div class="holder">
      <p class="holder__name">Evan Marlow</p>
      <p class="holder__title">Managing Director</p>
    </div>

    <div class="brand-tab">
      <svg width="332" height="58" viewBox="0 0 332 58" aria-hidden="true">
        <polygon points="24,0 332,0 332,58 0,58" fill="#f4f4f4"/>
      </svg>
      <div class="brand">
        <span class="brand__mark"></span>
        <span class="brand__name">Pale Ridge Software</span>
      </div>
    </div>

    <ul class="contact">
      <li><span class="contact__label">Office Phone:</span> 555-0142-7731</li>
      <li><span class="contact__label">Cell Phone:</span> 555-0142-7731</li>
      <li><span class="contact__label">Email:</span> contact@paleridgesoftware.example</li>
      <li><span class="contact__label">Web:</span> www.paleridgesoftware.example</li>
      <li><span class="contact__label">Address:</span> 4172 Wexmoor Pond Ave.,</li>
      <li>Ste. 2600, Bloomington, MN 55819</li>
    </ul>
  </section>
</main>
</body>
</html>
```